Brindlewood Property Management, L.L.C
Brindlewood Property Management, L.L.C - Financial Services
Creative Brief
Professional
Doreen Whitlock,CAM
President
P.O. Box 4821 Brindle Cove, FL. 30000
info@brindlewoodprop.com
www.brindlewoodprop.com
I am open to clear business cards or two sides if a two sided design is used see comment below.
Logo on back of card if this option is designed

```html
<!DOCTYPE html>
<html lang="en">
<head>
<meta charset="utf-8">
<title>Brindlewood Property Management – Stationery</title>
<link href="https://fonts.googleapis.com/css2?family=Open+Sans:wght@400;600;700&display=swap" rel="stylesheet">
<style>
  :root{
    --bg:#e7e4df;
    --paper:#ffffff;
    --navy:#0f2f6e;
    --blue:#1f56b3;
    --sky:#3f7fd6;
    --ink:#3a3f47;
    --muted:#8a9099;
    --rule:#c9ced6;
    --field:#eef1f6;
  }
  *{box-sizing:border-box;margin:0;padding:0}
  html,body{width:1200px;height:583px;overflow:hidden}
  body{background:var(--bg);font-family:"Open Sans",Arial,sans-serif;color:var(--ink);position:relative}
  .piece{position:absolute;background:var(--paper);box-shadow:0 2px 6px rgba(0,0,0,.18);overflow:hidden}

  .brand{display:flex;align-items:center;gap:6px}
  .brand-dot{border-radius:50%;background:var(--blue);flex:none}
  .brand-name{color:var(--navy);font-weight:700;line-height:1.1;text-transform:uppercase;letter-spacing:.3px;white-space:nowrap}

  .band{position:absolute;left:0;right:0;bottom:0;background:linear-gradient(90deg,var(--navy),var(--blue) 60%,var(--sky))}

  /* envelope back */
  .envelope-back{left:30px;top:40px;width:230px;height:300px}
  .envelope-back svg{display:block}

  /* envelope front */
  .envelope-front{left:30px;top:380px;width:300px;height:150px}
  .envelope-front .brand{position:absolute;left:14px;top:14px}
  .envelope-front .brand-dot{width:22px;height:22px}
  .envelope-front .brand-name{font-size:8px}
  .envelope-front .return{position:absolute;left:14px;top:42px;font-size:5.5px;color:var(--muted)}
  .envelope-front .band{height:14px}

  /* fax */
  .fax{left:290px;top:20px;width:310px;height:440px}
  .fax .brand{position:absolute;left:18px;top:18px}
  .fax .brand-dot{width:24px;height:24px}
  .fax .brand-name{font-size:8.5px}
  .fax .contact{position:absolute;right:18px;top:20px;font-size:5.5px;color:var(--muted);text-align:right;line-height:1.6}
  .fax-title{position:absolute;right:18px;top:62px;font-size:20px;font-weight:700;color:var(--navy);letter-spacing:2px}
  .fax-fields{position:absolute;left:18px;right:18px;top:96px;border-collapse:collapse;font-size:6.5px;table-layout:fixed}
  .fax-fields td{border:1px solid var(--rule);height:18px;padding:0 5px}
  .fax-fields .label{background:var(--field);color:var(--navy);font-weight:600;width:42px}
  .fax-checks{position:absolute;left:18px;right:18px;top:182px;display:flex;justify-content:space-between;font-size:5.5px;color:var(--ink)}
  .fax-checks span::before{content:"";display:inline-block;width:6px;height:6px;border:1px solid var(--muted);margin-right:3px;vertical-align:-1px}
  .fax-notes{position:absolute;left:18px;right:18px;top:202px;border-top:1px solid var(--rule)}
  .fax .band{height:14px}

  /* letterhead */
  .letterhead{left:625px;top:10px;width:340px;height:560px}
  .letterhead .brand{position:absolute;left:20px;top:18px}
  .letterhead .brand-dot{width:28px;height:28px}
  .letterhead .brand-name{font-size:10px}
  .letter-body{position:absolute;left:26px;right:26px;top:80px;font-size:6.2px;line-height:1.6}
  .letter-body p{margin-bottom:9px}
  .letter-body .recipient{margin-bottom:14px}
  .signature{width:70px;height:18px;background:var(--field);margin:4px 0}
  .letter-footer{position:absolute;left:0;right:0;bottom:18px;text-align:center;font-size:5.5px;color:var(--muted)}
  .letterhead .band{height:12px}

  /* business cards */
  .card{width:105px;height:60px}
  .card-front .brand{position:absolute;left:7px;top:7px;gap:4px}
  .card-front .brand-dot{width:12px;height:12px}
  .card-front .brand-name{font-size:4.6px}
  .card-front .details{position:absolute;left:7px;bottom:9px;font-size:3.8px;line-height:1.45;color:var(--ink);white-space:nowrap}
  .card-front .details strong{color:var(--navy);font-size:4.6px}
  .card-front .band{height:4px}
  .card-back{background:linear-gradient(135deg,var(--navy),var(--blue) 65%,var(--sky))}
  .card-back .brand-dot{position:absolute;left:50%;top:14px;width:18px;height:18px;margin-left:-9px;background:#fff}
  .card-back .url{position:absolute;left:0;right:0;bottom:11px;text-align:center;font-size:4.4px;color:#fff}
</style>
</head>
<body>

  <div class="piece envelope-back">
    <svg width="230" height="300" viewBox="0 0 230 300">
      <defs>
        <linearGradient id="flapShade" x1="0" y1="0" x2="0" y2="1">
          <stop offset="0" stop-color="#d9dde3"/>
          <stop offset="1" stop-color="#a9afb8"/>
        </linearGradient>
        <linearGradient id="flapBand" x1="0" y1="0" x2="1" y2="0">
          <stop offset="0" stop-color="#0f2f6e"/>
          <stop offset="1" stop-color="#3f7fd6"/>
        </linearGradient>
      </defs>
      <rect x="0" y="0" width="230" height="300" fill="#ffffff"/>
      <polygon points="0,0 230,0 230,40 115,170 0,40" fill="url(#flapShade)"/>
      <polygon points="0,40 115,170 230,40 230,52 115,182 0,52" fill="url(#flapBand)"/>
      <line x1="0" y1="300" x2="115" y2="182" stroke="#e1e4e9"/>
      <line x1="230" y1="300" x2="115" y2="182" stroke="#e1e4e9"/>
      <circle cx="115" cy="150" r="13" fill="#1f56b3"/>
    </svg>
  </div>

  <div class="piece envelope-front">
    <div class="brand">
      <span class="brand-dot"></span>
      <span class="brand-name">Brindlewood<br>Property Management</span>
    </div>
    <div class="return">P.O. Box 4821 Brindle Cove, FL. 30000</div>
    <div class="band"></div>
  </div>

  <div class="piece fax">
    <div class="brand">
      <span class="brand-dot"></span>
      <span class="brand-name">Brindlewood<br>Property Management</span>
    </div>
    <div class="contact">
      P.O. Box 4821 Brindle Cove, FL. 30000<br>
      Tel (000) 555-0142<br>
      info@brindlewoodprop.com<br>
      www.brindlewoodprop.com
    </div>
    <div class="fax-title">FAX</div>
    <table class="fax-fields">
      <tr><td class="label">To</td><td></td><td class="label">From</td><td></td></tr>
      <tr><td class="label">Fax</td><td></td><td class="label">Pages</td><td></td></tr>
      <tr><td class="label">Phone</td><td></td><td class="label">Date</td><td></td></tr>
      <tr><td class="label">Re</td><td></td><td class="label">CC</td><td></td></tr>
    </table>
    <div class="fax-checks">
      <span>Urgent</span><span>For Review</span><span>Please Comment</span><span>Please Reply</span><span>Please Recycle</span>
    </div>
    <div class="fax-notes"></div>
    <div class="band"></div>
  </div>

  <div class="piece letterhead">
    <div class="brand">
      <span class="brand-dot"></span>
      <span class="brand-name">Brindlewood<br>Property Management</span>
    </div>
    <div class="letter-body">
      <p class="recipient">Jordan Ellery<br>100 Harbor Street<br>Brindle Cove</p>
      <p>Dear Jordan Ellery,</p>
      <p>Thank you for choosing our team to care for your community. We manage budgets, vendor contracts and resident requests so your board can focus on long term planning and shared goals.</p>
      <p>Our staff will visit the property each month, review maintenance needs and prepare a clear report for every meeting. Questions can be sent by email at any time and we reply within one business day.</p>
      <p>Please find the proposed service agreement attached. We look forward to working with you and welcome any comments before the next board meeting.</p>
      <p>Kind Regards,</p>
      <div class="signature" role="img" aria-label="Handwritten signature"></div>
      <p>Doreen Whitlock,CAM</p>
    </div>
    <div class="letter-footer">P.O. Box 4821 Brindle Cove, FL. 30000 &nbsp;|&nbsp; info@brindlewoodprop.com &nbsp;|&nbsp; www.brindlewoodprop.com</div>
    <div class="band"></div>
  </div>

  <div class="piece card card-front" style="left:985px;top:200px">
    <div class="brand"><span class="brand-dot"></span><span class="brand-name">Brindlewood<br>Property Management</span></div>
    <div class="details"><strong>Doreen Whitlock,CAM</strong><br>President<br>P.O. Box 4821 Brindle Cove, FL. 30000<br>info@brindlewoodprop.com</div>
    <div class="band"></div>
  </div>
  <div class="piece card card-back" style="left:1100px;top:200px">
    <span class="brand-dot"></span>
    <div class="url">www.brindlewoodprop.com</div>
  </div>
  <div class="piece card card-front" style="left:985px;top:290px">
    <div class="brand"><span class="brand-dot"></span><span class="brand-name">Brindlewood<br>Property Management</span></div>
    <div class="details"><strong>Doreen Whitlock,CAM</strong><br>President<br>P.O. Box 4821 Brindle Cove, FL. 30000<br>www.brindlewoodprop.com</div>
    <div class="band"></div>
  </div>
  <div class="piece card card-back" style="left:1100px;top:290px">
    <span class="brand-dot"></span>
    <div class="url">brindlewoodprop.com</div>
  </div>

</body>
</html>
```